Halmi Rékas Physiotherapy Business Card Vienna

We need a business card design for a newly created Physiotherapy company based in Vienna Austria.
We seek a simple, modern, minimalist design without too much color variation. The font should look young/fresh, but definitely not childish or so. Since we are a starting Business, we currently haven't got a logo, if you feel like a logo would fit your design, feel free to use one, but it's not necessary.
Target Market(s)
Healthcare, young and elderly people with mobility issues
Industry/Entity Type
Health And Wellness
Contact Information for Business Card
Name: Réka Halmi
Title description: Physiotherapist
Phone num: +43 664 5290 4116
e-mail: reka.praxis@examplemail.net
Colors
Designer to choose colors to be used in the design.
Requirements
Must have
- Final design language must be in German, basically, the Title Description needs to be "Physiotherapeutin" the other details remain as in the English Language.
Nice to have
- Simple, modern, minimalist design
Should not have
- too many colors, Obvious use of a skeleton, skull, spline

```html
<!DOCTYPE html>
<html lang="de">
<head>
<meta charset="utf-8">
<title>Halmi Rékas Physiotherapy – Visitenkarte</title>
<link rel="stylesheet" href="https://fonts.googleapis.com/css2?family=Figtree:wght@500;700&display=swap">
<style>
  :root {
    --ink: #0b1117;
    --paper: #ffffff;
    --edge: #eef0f2;
    --rule: #1a2631;
  }
  * { margin: 0; padding: 0; box-sizing: border-box; }
  html, body { width: 1200px; height: 720px; overflow: hidden; background: var(--ink); }
  .card {
    position: relative;
    width: 1200px;
    height: 720px;
    background: var(--ink);
    font-family: "Figtree", "Helvetica Neue", Arial, sans-serif;
    color: var(--paper);
  }
  .edge {
    position: absolute;
    top: 96px;
    width: 40px;
    height: 525px;
    background: var(--edge);
    border-radius: 20px;
  }
  .edge--left { left: -20px; }
  .edge--right { right: -23px; }

  .brand {
    position: absolute;
    left: 84px;
    top: 194px;
    width: 400px;
    text-align: center;
  }
  .brand__ring {
    display: block;
    margin: 0 auto;
  }
  .brand__name {
    margin-top: 28px;
    font-weight: 700;
    font-size: 25px;
    letter-spacing: 0.5px;
    text-transform: uppercase;
    color: var(--paper);
    white-space: nowrap;
  }

  .timeline {
    position: absolute;
    left: 595px;
    top: 119px;
    width: 6px;
    height: 478px;
    background: repeating-linear-gradient(to bottom, var(--rule) 0 22px, transparent 22px 34px);
  }
  .contacts {
    position: absolute;
    left: 562px;
    top: 150px;
    list-style: none;
  }
  .contact {
    display: flex;
    align-items: center;
    height: 72px;
    margin-bottom: 38px;
  }
  .contact__icon {
    width: 72px;
    height: 72px;
    border-radius: 50%;
    background: var(--paper);
    display: flex;
    align-items: center;
    justify-content: center;
    flex-shrink: 0;
  }
  .contact__icon svg { width: 40px; height: 40px; fill: var(--ink); }
  .contact__text {
    margin-left: 20px;
    font-weight: 500;
    font-size: 33px;
    letter-spacing: 0.6px;
    white-space: nowrap;
  }
</style>
</head>
<body>
<main class="card">
  <div class="edge edge--left"></div>
  <div class="edge edge--right"></div>

  <div class="brand">
    <svg class="brand__ring" width="264" height="264" viewBox="0 0 264 264" aria-hidden="true">
      <circle cx="132" cy="132" r="124" fill="none" stroke="var(--paper)" stroke-width="15"/>
    </svg>
    <p class="brand__name">Halmi Rékas Physiotherapy</p>
  </div>

  <div class="timeline"></div>

  <ul class="contacts">
    <li class="contact">
      <span class="contact__icon">
        <svg viewBox="0 0 40 40" aria-hidden="true">
          <path d="M20 4c-5 0-8 3.5-8 8.5 0 5 3.4 10 8 10s8-5 8-10C28 7.5 25 4 20 4z"/>
          <path d="M4 36c0-6 5-9.5 11-10.5l5 4 5-4c6 1 11 4.5 11 10.5z"/>
        </svg>
      </span>
      <span class="contact__text">Réka Halmi</span>
    </li>
    <li class="contact">
      <span class="contact__icon">
        <svg viewBox="0 0 40 40" aria-hidden="true">
          <circle cx="17" cy="5" r="3.2"/>
          <path d="M15 10h4v9h9l4 9 2.6-1 1 2.6-5.4 2-4.4-9.6H15z"/>
          <path d="M12.5 16.5l.8 3.4A8.5 8.5 0 1 0 25 31l3 1.6A12 12 0 1 1 12.5 16.5z"/>
        </svg>
      </span>
      <span class="contact__text">Physiotherapeutin</span>
    </li>
    <li class="contact">
      <span class="contact__icon">
        <svg viewBox="0 0 40 40" aria-hidden="true">
          <path d="M9 5l5-1 4 8-3 3c1.5 3.5 4.5 6.5 8 8l3-3 8 4-1 5c-1 2-3 3-5 3C16 31 5 20 5 9c0-2 2-4 4-4z"/>
          <path d="M22 10a8 8 0 0 1 8 8h-2.4a5.6 5.6 0 0 0-5.6-5.6z"/>
          <path d="M22 4a14 14 0 0 1 14 14h-2.4A11.6 11.6 0 0 0 22 6.4z"/>
        </svg>
      </span>
      <span class="contact__text">+43 664 5290 4116</span>
    </li>
    <li class="contact">
      <span class="contact__icon">
        <svg viewBox="0 0 40 40" aria-hidden="true">
          <path d="M4 10h32v21H4z"/>
          <path d="M6 12l14 10 14-10" fill="none" stroke="#ffffff" stroke-width="2"/>
          <circle cx="20" cy="22" r="2.2" fill="#ffffff"/>
        </svg>
      </span>
      <span class="contact__text">reka.praxis@examplemail.net</span>
    </li>
  </ul>
</main>
</body>
</html>
```